Birchmead Assurance Group Ltd needs a business card and logo

We need a logo for documents, invoices etc and a business card to match. We are a health auditing, training and consulting company based in NZ and working in both Australia and NZ. We ensure health organisations meet all their compliance requirements and develop expertise in the health auditing sector. The design should in some way reflect either symbols for quality management in the health sector.

Target Market(s)

Health providers and those wishing to increase their capability in meeting and understanding compliance requirements

Industry/Entity Type

Business

Contact Information for Business Card

Logo plus contact details

Logo Text

Health auditing, consultancy and training

Requirements
Must have
• Name and contact details director: Clara Hotham, chotham@bag-example.co.nz, PO Box 419, Kereru Bay, NZ, cell +6427390516

```html
<!DOCTYPE html>
<html lang="en">
<head>
<meta charset="utf-8">
<title>Birchmead Assurance Group Ltd – Business Card</title>
<link rel="stylesheet" href="https://fonts.googleapis.com/css2?family=Quicksand:wght@500&family=Source+Sans+3:wght@400;600&display=swap">
<style>
  :root {
    --backdrop: #ece7df;
    --card-white: #ffffff;
    --card-black: #111111;
    --ink: #1a1a1a;
    --accent-red: #d0121b;
    --gold: #c9a227;
  }
  html, body {
    margin: 0;
    padding: 0;
    width: 1200px;
    height: 1200px;
    overflow: hidden;
    background: var(--backdrop);
  }
  .card {
    position: absolute;
    left: 287px;
    width: 626px;
    height: 390px;
    box-shadow: 0 12px 30px rgba(0,0,0,0.18);
  }
  .card--front { top: 150px; background: var(--card-white); }
  .card--back  { top: 680px; background: var(--card-black); }

  .brand {
    position: absolute;
    font-family: "Source Sans 3", sans-serif;
    font-weight: 600;
    color: var(--gold);
    display: flex;
    align-items: center;
    gap: 10px;
    margin: 0;
  }
  .brand__dot {
    flex: none;
    border-radius: 50%;
    background: var(--gold);
  }
  .card--front .brand {
    left: 44px;
    top: 166px;
    width: 250px;
    font-size: 22px;
    line-height: 1.15;
  }
  .card--front .brand__dot { width: 22px; height: 22px; }

  .card--back .brand {
    left: 0;
    right: 0;
    top: 182px;
    justify-content: center;
    font-size: 38px;
  }
  .card--back .brand__dot { width: 30px; height: 30px; }

  .divider {
    position: absolute;
    left: 322px;
    top: 106px;
    width: 2px;
    height: 179px;
    background: var(--accent-red);
  }
  .contact-block {
    position: absolute;
    left: 347px;
    top: 118px;
  }
  .person-name {
    font-family: "Quicksand", sans-serif;
    font-weight: 500;
    font-size: 27px;
    color: var(--ink);
    margin: 0;
    line-height: 1.1;
  }
  .person-role {
    font-family: "Quicksand", sans-serif;
    font-weight: 500;
    font-size: 16px;
    color: var(--accent-red);
    margin: 2px 0 22px;
  }
  .contact-list {
    list-style: none;
    margin: 0;
    padding: 0;
    font-family: "Source Sans 3", sans-serif;
    font-size: 16.5px;
    color: var(--ink);
  }
  .contact-list li {
    display: flex;
    align-items: center;
    gap: 11px;
    height: 28px;
    white-space: nowrap;
  }
  .contact-list svg { width: 14px; height: 14px; flex: none; fill: var(--accent-red); }
</style>
</head>
<body>
  <section class="card card--front">
    <p class="brand"><span class="brand__dot"></span>Birchmead Assurance Group Ltd</p>
    <div class="divider"></div>
    <div class="contact-block">
      <h1 class="person-name">Clara Hotham</h1>
      <p class="person-role">Director</p>
      <ul class="contact-list">
        <li>
          <svg viewBox="0 0 14 14" aria-hidden="true"><path d="M1 4h12v7H1z M1 4l6 4 6-4" fill="var(--accent-red)" stroke="#fff" stroke-width="0.8"/></svg>
          chotham@bag-example.co.nz
        </li>
        <li>
          <svg viewBox="0 0 14 14" aria-hidden="true"><path d="M4 1h6a1 1 0 0 1 1 1v10a1 1 0 0 1-1 1H4a1 1 0 0 1-1-1V2a1 1 0 0 1 1-1zm0.6 1.5v8h4.8v-8z"/></svg>
          +6427390516
        </li>
        <li>
          <svg viewBox="0 0 14 14" aria-hidden="true"><path d="M7 0.5a4.5 4.5 0 0 1 4.5 4.5c0 3.2-4.5 8.5-4.5 8.5S2.5 8.2 2.5 5A4.5 4.5 0 0 1 7 0.5zm0 2.8a1.7 1.7 0 1 0 0 3.4 1.7 1.7 0 0 0 0-3.4z"/></svg>
          PO Box 419, Kereru Bay, NZ,
        </li>
      </ul>
    </div>
  </section>

  <section class="card card--back">
    <p class="brand"><span class="brand__dot"></span>Birchmead Assurance Group Ltd</p>
  </section>
</body>
</html>
```